Business Card Re-Design for a Lighting Designer

I would like my business card re-designed. It is currently high gloss and they scratch too easily. I don not think the current design lends itself well to a matte finish. I have included the current design for reference along with our company logo.
Check out our website for current branding.
http://www.brambleorchidstudio.example

Updates
Some of the top contenders are muslim and it is a holiday for them. I do not want to discriminate and would expect the same courtesy for holidays we celebrate.
Target Market(s)
Interior Designers, Architects
Contact Information for Business Card
Logo - Name, Title, Address, Telephone Number and Extension, Email
Font styles to use
Requirements
Must have
- All the information listed on the current business card. If you use Red, it needs to be the red from our logo.
Nice to have
- Vertical and Horizontal Designs will be entertained.
Should not have
- Requirements for a glossy finish...should not look too corporate since we are a design firm.

```html
<!DOCTYPE html>
<html lang="en">
<head>
<meta charset="utf-8">
<title>Bramble Orchid Studio – Business Card</title>
<link href="https://fonts.googleapis.com/css2?family=Montserrat:wght@300;400;600&display=swap" rel="stylesheet">
<style>
  :root {
    --backdrop: #3a3a3c;
    --card-white: #ffffff;
    --brand-red: #a31c22;
    --brand-red-deep: #8f1a1f;
    --brand-red-light: #b8262c;
    --ink: #3b3b3b;
    --ink-soft: #8a8a8a;
  }
  * { margin: 0; padding: 0; box-sizing: border-box; }
  html, body {
    width: 1200px; height: 900px; overflow: hidden;
    background: var(--backdrop);
    font-family: "Montserrat", sans-serif;
  }
  .canvas { position: relative; width: 1200px; height: 900px; }

  .card {
    position: absolute;
    width: 525px; height: 300px;
    border-radius: 3px;
    box-shadow: 0 14px 30px rgba(0,0,0,0.35);
  }

  /* Back side */
  .card--back {
    left: 620px; top: 150px;
    background: linear-gradient(135deg, var(--brand-red-light), var(--brand-red-deep));
    display: flex; align-items: center; justify-content: center; gap: 18px;
  }
  .back-mark {
    width: 70px; height: 70px;
    background: var(--brand-red);
    border: 1px solid rgba(0,0,0,0.12);
  }
  .back-name {
    color: #951a20;
    font-weight: 300; font-size: 34px; line-height: 1.05;
    text-transform: uppercase; letter-spacing: 1px;
  }

  /* Front side */
  .card--front {
    left: 55px; top: 450px;
    background: var(--card-white);
    padding: 26px 30px;
    color: var(--ink);
  }
  .brand {
    display: flex; align-items: flex-end; gap: 12px;
  }
  .brand-square {
    width: 58px; height: 58px; background: var(--brand-red);
  }
  .brand-name {
    font-weight: 300; font-size: 21px; line-height: 1.05;
    text-transform: uppercase; color: var(--ink);
  }
  .divider {
    position: absolute; left: 30px; top: 118px;
    width: 400px; height: 1px; background: var(--brand-red);
  }
  .contact {
    position: absolute; left: 30px; top: 150px;
    font-size: 13px; font-weight: 400; line-height: 1.6;
  }
  .person {
    position: absolute; right: 30px; top: 138px;
    text-align: right;
  }
  .person-name {
    color: var(--brand-red); font-weight: 600; font-size: 17px;
    text-transform: uppercase; letter-spacing: 0.3px;
  }
  .person-title { font-size: 14px; font-weight: 400; margin-bottom: 8px; }
  .person-address { font-size: 13px; line-height: 1.5; }
</style>
</head>
<body>
  <main class="canvas">
    <section class="card card--back">
      <div class="back-mark"></div>
      <div class="back-name">Bramble<br>Orchid Studio</div>
    </section>

    <section class="card card--front">
      <div class="brand">
        <div class="brand-square"></div>
        <div class="brand-name">Bramble<br>Orchid Studio</div>
      </div>
      <div class="divider"></div>
      <div class="contact">
        <p>555 014 2280 X1</p>
        <p>maren@brambleorchidstudio.example</p>
        <p>www.brambleorchidstudio.example</p>
      </div>
      <div class="person">
        <p class="person-name">Maren Holloway</p>
        <p class="person-title">Principal</p>
        <p class="person-address">212 Larkspur Row<br>Suite 40, Fairhaven<br>Oregon 97000 USA</p>
      </div>
    </section>
  </main>
</body>
</html>
```